CAR PAINT AEROSOL

car paint aerosol
3 different aerosols
x1 paint
x1 lacquer
x1 primer

We want something eye catching that will outshine competitors this is automotive paint, we are looking for something modern and clean. Will require a logo as well as the can design too. We have added our 'KMV' brand that is already competitive on the market but this looks very 'trade' style so looking for something more retail (will attach photos of our current aerosols) . Please note we are looking for a new brand name, logo and design. So a completely different brand and look to our current KMV aerosols.
examples of competitors attached

label template attached

Target Market(s)

AUTOMOTIVE INDUSTRY TO RETAIL BUYERS,

Industry/Entity Type

car paint

Requirements
Must have
• NEW BRAND NAME , LOGO AND DESIGN
Nice to have
• own domain www.glenvarnish.co.uk not essential to design but would be good for brand to tie in
Should not have
• ideally not red as current brand is

```html
<!DOCTYPE html>
<html lang="en">
<head>
<meta charset="utf-8">
<title>VARNO Aerosol Labels – Lacquer, Paint, Primer</title>
<link href="https://fonts.googleapis.com/css2?family=Oswald:wght@500;700&display=swap" rel="stylesheet">
<style>
  :root {
    --bg: #050505;
    --ink: #ffffff;
    --band: #0a0a0a;
    --silver-hi: #e9e9e9;
    --silver-mid: #a9a9a9;
    --silver-lo: #3a3a3a;
    --gold-hi: #f4dc9a;
    --gold-mid: #c9a24e;
    --gold-lo: #3b2a0e;
    --copper-hi: #f0c3a0;
    --copper-mid: #b46a3e;
    --copper-lo: #3a1a0c;
  }
  * { box-sizing: border-box; margin: 0; padding: 0; }
  html, body {
    width: 1200px; height: 960px; overflow: hidden;
    background: var(--bg);
    font-family: "Oswald", "Arial Narrow", sans-serif;
    color: var(--ink);
  }
  .label-set {
    width: 1200px; height: 960px;
    display: flex; justify-content: center; align-items: center; gap: 48px;
  }
  .label {
    position: relative;
    width: 330px; height: 820px;
    border-radius: 6px;
    overflow: hidden;
    display: flex; flex-direction: column;
    background: var(--band);
  }
  .label--lacquer { --hi: var(--silver-hi); --mid: var(--silver-mid); --lo: var(--silver-lo); }
  .label--paint   { --hi: var(--gold-hi);   --mid: var(--gold-mid);   --lo: var(--gold-lo); }
  .label--primer  { --hi: var(--copper-hi); --mid: var(--copper-mid); --lo: var(--copper-lo); }

  .label__photo {
    height: 200px;
    background: linear-gradient(160deg, var(--hi) 0%, var(--mid) 55%, var(--lo) 100%);
  }
  .label__waves {
    position: relative;
    flex: 1;
    background: linear-gradient(180deg, var(--mid) 0%, var(--lo) 70%, var(--band) 100%);
  }
  .brand {
    position: absolute;
    left: 50%; top: 50%;
    transform: translate(-50%, -50%) rotate(-90deg);
    font-weight: 700;
    font-size: 150px;
    line-height: 1;
    letter-spacing: 4px;
    color: var(--hi);
    white-space: nowrap;
  }
  .label__band {
    height: 190px;
    padding: 0 26px 34px;
    display: flex; flex-direction: column; justify-content: flex-end; align-items: center;
    background: var(--band);
    border-bottom: 6px solid var(--mid);
  }
  .product-name {
    font-weight: 500;
    font-size: 78px;
    line-height: 1;
    letter-spacing: 1px;
  }
  .tagline {
    margin-top: 10px;
    font-weight: 500;
    font-size: 13px;
    letter-spacing: 0.5px;
    text-transform: uppercase;
  }
</style>
</head>
<body>
  <main class="label-set">
    <section class="label label--lacquer">
      <div class="label__photo" role="img" aria-label="Silver-toned photo of a car being sprayed with a paint gun"></div>
      <div class="label__waves" role="img" aria-label="Silver flowing line pattern">
        <span class="brand">VARNO</span>
      </div>
      <div class="label__band">
        <h2 class="product-name">LACQUER</h2>
        <p class="tagline">Automotive and industrial coatings</p>
      </div>
    </section>

    <section class="label label--paint">
      <div class="label__photo" role="img" aria-label="Gold-toned photo of a car being sprayed with a paint gun"></div>
      <div class="label__waves" role="img" aria-label="Gold flowing line pattern">
        <span class="brand">VARNO</span>
      </div>
      <div class="label__band">
        <h2 class="product-name">PAINT</h2>
        <p class="tagline">Automotive and industrial coatings</p>
      </div>
    </section>

    <section class="label label--primer">
      <div class="label__photo" role="img" aria-label="Copper-toned photo of a car being sprayed with a paint gun"></div>
      <div class="label__waves" role="img" aria-label="Copper flowing line pattern">
        <span class="brand">VARNO</span>
      </div>
      <div class="label__band">
        <h2 class="product-name">PRIMER</h2>
        <p class="tagline">Automotive and industrial coatings</p>
      </div>
    </section>
  </main>
</body>
</html>
```